FREIGHT FORWARDING FLYER

We need a flyer designed for our company (Brightwell Freight Global) showing the list of services we offer to hand out to customers. Below is a list of services:<br/><br/>-Ocean/Air Import and Export<br/>-Exhibition Cargo<br/>-Carnet Application<br/>-Project Cargo (OOG/Flatrack/Reefer/DG)<br/>-Customs Clearance<br/>-Door to Door Services<br/>-Cargo Insurance<br/>-Warehousing<br/>-Trucking (LTL/FCL)

Target Market(s)

Customers who have a specific need for freight forwarding, especially customers at exhibitions.

Industry/Entity Type

Freight Forwarding

Colors

Designer to choose colors to be used in the design.

Requirements
Must have
• The services we offer need to pop to the customer and essentially get that interested in the services we offer.

```html
<!DOCTYPE html>
<html lang="en">
<head>
<meta charset="utf-8">
<title>Brightwell Freight Global – List of Services</title>
<link rel="stylesheet" href="https://fonts.googleapis.com/css2?family=Bebas+Neue&family=Rajdhani:wght@600&display=swap">
<style>
  :root {
    --stage: #e9e6e1;
    --flyer-black: #0d0d0d;
    --ink-white: #ffffff;
    --accent-blue: #1e8fd6;
    --accent-red: #e0222c;
    --photo-warm: #c99a4a;
    --photo-teal: #2c7f86;
    --photo-navy: #0e2f57;
  }
  * { margin: 0; padding: 0; box-sizing: border-box; }
  html, body {
    width: 1200px; height: 800px; overflow: hidden;
    background: var(--stage);
  }
  .flyer {
    position: absolute; left: 334px; top: 20px;
    width: 532px; height: 760px;
    background: var(--flyer-black);
    overflow: hidden;
    box-shadow: 0 6px 24px rgba(0,0,0,.25);
  }
  .flyer-art { position: absolute; inset: 0; width: 100%; height: 100%; }
  .brand {
    position: absolute; left: 34px; top: 30px;
    display: flex; align-items: center; gap: 10px;
  }
  .brand-mark { width: 30px; height: 30px; background: var(--accent-red); }
  .brand-name {
    font-family: "Bebas Neue", sans-serif;
    font-size: 26px; letter-spacing: 1px;
    color: var(--ink-white);
  }
  .headline {
    position: absolute; left: 34px; top: 108px;
    font-family: "Bebas Neue", sans-serif;
    font-size: 35px; letter-spacing: .3px;
    color: var(--ink-white); white-space: nowrap;
  }
  .headline .highlight { color: var(--accent-blue); }
  .service-list { position: absolute; left: 34px; top: 0; list-style: none; }
  .service {
    position: absolute; left: 0;
    display: flex; align-items: center; gap: 9px;
    white-space: nowrap; transform: translateY(-50%);
    font-family: "Rajdhani", sans-serif; font-weight: 600;
    font-size: 13px; letter-spacing: .4px; text-transform: uppercase;
    color: var(--ink-white);
  }
  .service svg { width: 26px; height: 26px; flex: none; }
  .service small { font-size: 9px; margin-left: -5px; }
  .icon { fill: none; stroke: var(--accent-red); stroke-width: 2; }
  .icon-fill { fill: var(--accent-red); }
</style>
</head>
<body>
<main class="flyer">
  <svg class="flyer-art" viewBox="0 0 532 760" preserveAspectRatio="none">
    <defs>
      <linearGradient id="photo-tone" x1="0" y1="0" x2="0" y2="1">
        <stop offset="0" stop-color="var(--photo-teal)"/>
        <stop offset=".55" stop-color="var(--photo-warm)"/>
        <stop offset="1" stop-color="var(--photo-navy)"/>
      </linearGradient>
    </defs>
    <polygon class="harbour-photo" role="img" aria-label="Photo of a container port at sunset with cranes, cargo ships and reflections on the water"
      points="532,110 532,760 0,760 0,650" fill="url(#photo-tone)"/>
  </svg>

  <header class="brand">
    <span class="brand-mark"></span>
    <span class="brand-name">Brightwell Freight Global</span>
  </header>

  <h1 class="headline">List of <span class="highlight">Services</span> we offer</h1>

  <ul class="service-list">
    <li class="service" style="top:190px">
      <svg viewBox="0 0 26 26"><circle class="icon" cx="11" cy="14" r="8"/><path class="icon" d="M3 14h16M11 6c-4 5-4 11 0 16M11 6c4 5 4 11 0 16"/><rect class="icon-fill" x="16" y="3" width="8" height="6"/></svg>
      Ocean/Air Import and Export
    </li>
    <li class="service" style="top:225px">
      <svg viewBox="0 0 26 26"><rect class="icon" x="3" y="3" width="20" height="13"/><circle class="icon-fill" cx="10" cy="19" r="2"/><circle class="icon-fill" cx="16" cy="19" r="2"/><path class="icon" d="M10 21v4M16 21v4"/></svg>
      Exhibition Cargo
    </li>
    <li class="service" style="top:260px">
      <svg viewBox="0 0 26 26"><rect class="icon-fill" x="2" y="5" width="22" height="16"/><rect x="5" y="9" width="6" height="6" fill="#0d0d0d"/><path d="M13 10h8M13 14h8M5 18h16" stroke="#0d0d0d" stroke-width="1.5"/></svg>
      Carnet Application
    </li>
    <li class="service" style="top:294px">
      <svg viewBox="0 0 26 26"><rect class="icon" x="3" y="2" width="20" height="15"/><path class="icon-fill" d="M8 14h2v-4H8zM12 14h2V7h-2zM16 14h2V9h-2z"/><path class="icon" d="M9 17l-3 8M17 17l3 8"/></svg>
      Project Cargo (OOG/Flatrack/Reefer/DG)
    </li>
    <li class="service" style="top:329px">
      <svg viewBox="0 0 26 26"><rect class="icon" x="4" y="2" width="14" height="22"/><path class="icon" d="M7 7h8M7 11h8M7 15h5"/><circle class="icon-fill" cx="20" cy="20" r="4"/></svg>
      Customs Clearance
    </li>
    <li class="service" style="top:363px">
      <svg viewBox="0 0 26 26"><rect class="icon" x="13" y="2" width="11" height="22"/><circle class="icon-fill" cx="7" cy="6" r="3"/><path class="icon" d="M7 10v8l-3 6M7 18l3 6M3 13h9"/></svg>
      Door to Door Services
    </li>
    <li class="service" style="top:398px">
      <svg viewBox="0 0 26 26"><rect class="icon" x="2" y="4" width="10" height="18"/><path class="icon" d="M17 4l7 3v6c0 5-3 8-7 10-4-2-7-5-7-10V7z"/></svg>
      Cargo Insurance
    </li>
    <li class="service" style="top:432px">
      <svg viewBox="0 0 26 26"><path class="icon-fill" d="M2 10L13 3l11 7v14H2z"/><rect x="8" y="13" width="10" height="11" fill="#0d0d0d"/><path d="M9 16h8M9 19h8M9 22h8" stroke="var(--accent-red)" stroke-width="1.5"/></svg>
      Warehousing
    </li>
    <li class="service" style="top:466px">
      <svg viewBox="0 0 26 26"><rect class="icon-fill" x="1" y="7" width="16" height="11"/><path class="icon-fill" d="M18 10h4l3 4v4h-7z"/><circle cx="6" cy="20" r="2.5" fill="var(--accent-red)" stroke="#0d0d0d"/><circle cx="20" cy="20" r="2.5" fill="var(--accent-red)" stroke="#0d0d0d"/></svg>
      Trucking <small>(LTL/FCL)</small>
    </li>
  </ul>
</main>
</body>
</html>
```